bramblecrest paving card makeover

were a excavation/paving contractor from Monterey ca, I'm looking to have a card designed front and back that has company details on the front and a list of the services we offer on the back.

Target Market(s)

home owners property management companies

Industry/Entity Type

Contractor

Contact Information for Business Card

bramblecrest paving 418 larkmoor st Monterey ca. licensed, insured and bonded
lic#657920 gerald pinsky operations manager

Font styles to use
Serif
Sans Serif

Colors
f78f20

Requirements
Must have
• a list of my services on back, asphalt construction and maintenance, drainage, foundations, retaining walls, chip seals, excavation, grading, landscape ground work, interlocking paver, hydro-seeding, structured and driveway demolition, utility trenching and stump removal.
Nice to have
• my new domain and page address I'm acquiring from pixel bazaar.

```html
<!DOCTYPE html>
<html lang="en">
<head>
<meta charset="utf-8">
<title>Bramblecrest Paving – Business Card</title>
<link href="https://fonts.googleapis.com/css2?family=Roboto:wght@400;500;700;900&display=swap" rel="stylesheet">
<style>
  :root {
    --orange: #f78f20;
    --ink: #141414;
    --card-dark: #1c1c1e;
    --paper: #ffffff;
    --stage: #3a3a3c;
    --muted: #8a8a8e;
    --soft: #b4b4b8;
  }
  * { margin: 0; padding: 0; box-sizing: border-box; }
  html, body { width: 799px; height: 1200px; overflow: hidden; }
  body {
    background: var(--stage);
    font-family: "Roboto", Arial, sans-serif;
    position: relative;
  }
  .card {
    position: absolute;
    left: 70px;
    width: 660px;
    height: 378px;
    border-radius: 26px;
    overflow: hidden;
  }
  .card--front { top: 111px; background: var(--card-dark); }
  .card--back { top: 711px; background: var(--paper); }

  .brand-mark {
    position: absolute;
    display: flex;
    align-items: center;
    gap: 14px;
    white-space: nowrap;
  }
  .brand-mark__dot {
    width: 34px; height: 34px;
    border-radius: 50%;
    background: var(--muted);
    flex: none;
  }
  .brand-mark__name {
    font-weight: 900;
    font-size: 30px;
    letter-spacing: 0.5px;
    text-transform: uppercase;
    color: var(--muted);
  }
  .card--front .brand-mark {
    left: 50%; top: 78px;
    transform: translateX(-50%);
  }

  .services {
    position: absolute;
    left: 50px; right: 50px; top: 160px;
    text-align: center;
    color: var(--soft);
  }
  .services__title {
    font-size: 13px;
    font-weight: 700;
    letter-spacing: 3px;
    text-transform: uppercase;
    color: var(--orange);
    margin-bottom: 14px;
  }
  .services__list {
    list-style: none;
    display: flex;
    flex-wrap: wrap;
    justify-content: center;
    gap: 8px 0;
    font-size: 14px;
    line-height: 1.3;
  }
  .services__list li { white-space: nowrap; }
  .services__list li + li::before {
    content: "•";
    color: var(--orange);
    margin: 0 9px;
  }

  .card--back .brand-mark { left: 32px; top: 66px; gap: 12px; }
  .card--back .brand-mark__dot { background: var(--ink); width: 26px; height: 26px; }
  .card--back .brand-mark__name { color: var(--ink); font-size: 20px; }

  .swoosh { position: absolute; inset: 0; width: 100%; height: 100%; }

  .company {
    position: absolute;
    right: 38px; top: 36px;
    text-align: right;
    color: var(--ink);
  }
  .company__name {
    font-weight: 900;
    font-size: 26px;
    color: var(--orange);
    margin-bottom: 4px;
  }
  .company__person { font-size: 17px; font-weight: 700; line-height: 1.35; }
  .company__role { font-size: 14px; color: #555; line-height: 1.35; margin-bottom: 4px; }
  .company__line { font-size: 16px; line-height: 1.45; }

  .contact {
    position: absolute;
    right: 30px; bottom: 22px;
    list-style: none;
    color: var(--paper);
    font-size: 17px;
    line-height: 1.5;
    text-align: right;
  }
  .contact li { display: flex; justify-content: flex-end; align-items: center; gap: 10px; }
  .contact .accent { color: var(--orange); }
  .contact svg { width: 15px; height: 15px; fill: var(--orange); flex: none; }
</style>
</head>
<body>

<section class="card card--front" aria-label="Card front">
  <div class="brand-mark">
    <span class="brand-mark__dot"></span>
    <span class="brand-mark__name">Bramblecrest Paving</span>
  </div>
  <div class="services">
    <p class="services__title">Our Services</p>
    <ul class="services__list">
      <li>Asphalt Construction &amp; Maintenance</li>
      <li>Drainage</li>
      <li>Foundations</li>
      <li>Retaining Walls</li>
      <li>Chip Seals</li>
      <li>Excavation</li>
      <li>Grading</li>
      <li>Landscape Ground Work</li>
      <li>Interlocking Paver</li>
      <li>Hydro-Seeding</li>
      <li>Structure &amp; Driveway Demolition</li>
      <li>Utility Trenching</li>
      <li>Stump Removal</li>
    </ul>
  </div>
</section>

<section class="card card--back" aria-label="Card back">
  <svg class="swoosh" viewBox="0 0 660 378" preserveAspectRatio="none" aria-hidden="true">
    <path d="M0,205 C160,225 220,300 380,285 C500,272 580,240 660,255 L660,378 L0,378 Z" fill="var(--ink)"/>
    <path d="M0,180 C150,200 230,270 390,262 C510,256 590,230 660,240 L660,252 C590,242 510,270 390,280 C220,292 150,222 0,200 Z" fill="var(--orange)"/>
    <path d="M60,205 C170,220 240,250 380,248 C500,246 590,222 660,222 L660,228 C590,230 500,256 380,258 C240,260 170,230 60,205 Z" fill="var(--orange)"/>
  </svg>

  <div class="brand-mark">
    <span class="brand-mark__dot"></span>
    <span class="brand-mark__name">Bramblecrest Paving</span>
  </div>

  <div class="company">
    <p class="company__name">Bramblecrest Paving</p>
    <p class="company__person">Gerald Pinsky</p>
    <p class="company__role">Operations Manager</p>
    <p class="company__line">Lic # 657920</p>
    <p class="company__line">Licensed, Insured &amp; Bonded</p>
  </div>

  <ul class="contact">
    <li><span>(012) 555 0147</span>
      <svg viewBox="0 0 16 16"><path d="M3 1h3l1.5 4-2 1.2a9 9 0 0 0 4.3 4.3L11 8.5l4 1.5v3a2 2 0 0 1-2 2A12 12 0 0 1 1 3a2 2 0 0 1 2-2z"/></svg>
    </li>
    <li><span>info@bramblecrestpaving.com</span>
      <svg viewBox="0 0 16 16"><path d="M1 3h14v10H1z M1 3l7 6 7-6" fill="var(--orange)" stroke="var(--ink)" stroke-width="1.2"/></svg>
    </li>
    <li><span>www.<span class="accent">bramblecrestpaving</span>.com</span>
      <svg viewBox="0 0 16 16"><circle cx="8" cy="8" r="7"/><path d="M1 8h14M8 1c-3 3-3 11 0 14M8 1c3 3 3 11 0 14" stroke="var(--ink)" stroke-width="1" fill="none"/></svg>
    </li>
    <li><span>418 larkmoor ST Monterey CA</span>
      <svg viewBox="0 0 16 16"><path d="M8 0a5.5 5.5 0 0 1 5.5 5.5C13.5 10 8 16 8 16S2.5 10 2.5 5.5A5.5 5.5 0 0 1 8 0z"/><circle cx="8" cy="5.5" r="2" fill="var(--ink)"/></svg>
    </li>
  </ul>
</section>

</body>
</html>
```